BUsiness Card

We need a unique business card design for a new aesthetic practice, Meadowlark Aesthetics & Wellness, P.A. The reverse of the card should be an appointment card.

```html
<!DOCTYPE html>
<html lang="en">
<head>
<meta charset="utf-8">
<title>Meadowlark Aesthetics &amp; Wellness – Business Card</title>
<link rel="stylesheet" href="https://fonts.googleapis.com/css2?family=Roboto:ital,wght@0,400;0,500;1,400&family=Roboto+Condensed:wght@400;700&display=swap">
<style>
  :root {
    --navy: #0d4a68;
    --teal: #4fbfc1;
    --teal-light: #9fd9da;
    --ink: #4a4a4a;
    --muted: #666;
    --paper: #f4f4f4;
    --backdrop: #2b2b2b;
  }
  * { box-sizing: border-box; margin: 0; padding: 0; }
  html, body { width: 1200px; height: 960px; overflow: hidden; }
  body { background: var(--backdrop); font-family: "Roboto", sans-serif; position: relative; }

  .card {
    position: absolute; width: 600px; height: 342px;
    background: var(--paper); box-shadow: 0 2px 6px rgba(0,0,0,.5); overflow: hidden;
  }
  .card-front { left: 321px; top: 110px; }
  .card-back { left: 320px; top: 493px; }

  /* front */
  .brand { position: absolute; left: 30px; top: 98px; width: 255px; text-align: center; color: var(--navy); }
  .brand-mark { display: block; margin: 0 auto 10px; }
  .brand-name { font-family: "Roboto", sans-serif; font-weight: 500; font-size: 34px; line-height: 1; }
  .brand-sub { font-family: "Roboto", sans-serif; font-weight: 500; font-size: 13.5px; line-height: 1.2; margin-top: 4px; letter-spacing: .5px; }
  .divider { position: absolute; left: 299px; top: 75px; width: 2px; height: 195px; background: linear-gradient(to bottom, transparent, #cfcfcf 20%, #cfcfcf 80%, transparent); }
  .contact { position: absolute; left: 326px; top: 82px; }
  .person-name { font-family: "Roboto Condensed", sans-serif; font-weight: 700; font-size: 24px; color: var(--navy); line-height: 1; }
  .person-role { font-family: "Roboto Condensed", sans-serif; font-size: 16px; color: var(--teal); margin-top: 3px; }
  .address { font-size: 14px; color: var(--ink); line-height: 18px; margin-top: 9px; }
  .contact-list { list-style: none; margin-top: 12px; font-size: 14px; color: var(--ink); line-height: 19px; }
  .contact-list li { display: flex; align-items: center; gap: 7px; }
  .contact-list svg { width: 13px; height: 13px; fill: var(--navy); flex: none; }
  .band-light { position: absolute; left: 0; right: 0; top: 318px; height: 3px; background: var(--teal-light); }
  .band-dark { position: absolute; left: 0; right: 0; top: 322px; height: 20px; background: var(--navy); }

  /* back */
  .faint-circle { position: absolute; left: 150px; top: 50px; width: 270px; height: 270px; border-radius: 50%; background: #e6e8ea; opacity: .7; }
  .appt { position: absolute; inset: 0; padding: 0 38px 0 32px; color: var(--navy); }
  .appt-title { text-align: center; font-weight: 500; font-size: 25px; margin-top: 36px; }
  .field { display: flex; align-items: baseline; font-size: 15px; }
  .field .fill { flex: 1; border-bottom: 2px dotted #8a8a8a; margin-left: 8px; height: 12px; }
  .row-name { margin-top: 18px; }
  .row-date { margin-top: 27px; }
  .row-date .date-fill { flex: 0 0 228px; }
  .row-date .time-label { margin-left: 24px; }
  .row-date .time-fill { flex: 0 0 125px; margin-right: 3px; }
  .days { display: flex; justify-content: space-between; margin-top: 30px; font-size: 15px; }
  .day { display: flex; align-items: center; gap: 8px; }
  .box { width: 17px; height: 15px; border: 1.5px solid #555; border-radius: 2px; background: #fff; }
  .row-note { margin-top: 26px; }
  .row-blank { margin-top: 24px; }
  .row-blank .fill { margin-left: 0; }
  .policy { text-align: center; font-style: italic; font-size: 14px; color: var(--muted); line-height: 17px; margin-top: 26px; }
</style>
</head>
<body>

<section class="card card-front" aria-label="Business card front">
  <div class="brand">
    <svg class="brand-mark" width="92" height="92" viewBox="0 0 92 92" aria-hidden="true"><circle cx="46" cy="46" r="46" fill="#0d4a68"/></svg>
    <div class="brand-name">Meadowlark</div>
    <div class="brand-sub">Aesthetics &amp; Wellness</div>
  </div>
  <div class="divider"></div>
  <div class="contact">
    <div class="person-name">DANIEL REYES</div>
    <div class="person-role">CEO/FOUNDER</div>
    <p class="address">Meadowlark Aesthetics &amp; Wellness, P.A.<br>4120 Willow Bend Road<br>Juneau, Alaska 99801</p>
    <ul class="contact-list">
      <li><svg viewBox="0 0 24 24"><path d="M6.6 10.8a15.2 15.2 0 0 0 6.6 6.6l2.2-2.2a1 1 0 0 1 1-.25 11.4 11.4 0 0 0 3.6.57 1 1 0 0 1 1 1V20a1 1 0 0 1-1 1A17 17 0 0 1 3 4a1 1 0 0 1 1-1h3.5a1 1 0 0 1 1 1c0 1.25.2 2.45.57 3.6a1 1 0 0 1-.25 1z"/></svg>555 214 7730</li>
      <li><svg viewBox="0 0 24 24"><path d="M2 5h20v2l-10 6L2 7z M2 9l10 6 10-6v10H2z"/></svg>dreyes@meadowlarkaesthetics.com</li>
      <li><svg viewBox="0 0 24 24"><path d="M12 2a10 10 0 1 0 0 20 10 10 0 0 0 0-20zm-1 17.9A8 8 0 0 1 4.1 10H7l2 2v2l2 2zm6.9-2.5A2 2 0 0 0 16 16h-1v-3a1 1 0 0 0-1-1H8v-2h2a1 1 0 0 0 1-1V7h2a2 2 0 0 0 2-2v-.4a8 8 0 0 1 2.9 12.8z"/></svg>www.meadowlarkaesthetics.com</li>
    </ul>
  </div>
  <div class="band-light"></div>
  <div class="band-dark"></div>
</section>

<section class="card card-back" aria-label="Appointment card">
  <div class="faint-circle" aria-hidden="true"></div>
  <div class="appt">
    <h2 class="appt-title">Next Appointment</h2>
    <div class="field row-name"><span>Name :</span><span class="fill"></span></div>
    <div class="field row-date"><span>Date :</span><span class="fill date-fill"></span><span class="time-label">Time :</span><span class="fill time-fill"></span><span>AM/PM</span></div>
    <div class="days">
      <span class="day">Sun <span class="box"></span></span>
      <span class="day">Mon <span class="box"></span></span>
      <span class="day">Tue <span class="box"></span></span>
      <span class="day">Wed <span class="box"></span></span>
      <span class="day">Thu <span class="box"></span></span>
      <span class="day">Fri <span class="box"></span></span>
      <span class="day">Sat <span class="box"></span></span>
    </div>
    <div class="field row-note"><span>Note :</span><span class="fill"></span></div>
    <div class="field row-blank"><span class="fill"></span></div>
    <p class="policy">Please give me 24 hours notice if you are unable to keep your<br>appointment or a cancellation fee may be charged.</p>
  </div>
</section>

</body>
</html>
```